business card for Your Loan Scout

Please create a business card for my new business. I have attached another business card i have used previously and I like its layout and the hologram style backing with the logo. Replace the information with my new business information. On the information side of the card under the logo please place the TLCA acredited member logo I have uploaded along with 'Credit Rep Number 381749'.
next to my name in smaller text and not bold write 'JP'. and my title change from director to Broker/Director
Industry/Entity Type
Mortgage Brokerage
Contact Information for Business Card
As already on the uploaded card and in project description
Colors
Designer to choose colors to be used in the design.
Look and feel
Each slider illustrates characteristics of the customer's brand and the style your logo design should communicate.

```html
<!DOCTYPE html>
<html lang="en">
<head>
<meta charset="utf-8">
<title>Your Loan Scout – Business Card</title>
<link href="https://fonts.googleapis.com/css2?family=Lato:wght@400;700&display=swap" rel="stylesheet">
<style>
  :root {
    --backdrop: #607f88;
    --card: #ffffff;
    --brand-blue: #0b78be;
    --brand-grey: #7a8c9c;
    --ink-light: #ffffff;
  }
  html, body {
    margin: 0;
    width: 1200px;
    height: 1200px;
    overflow: hidden;
    background: var(--backdrop);
    font-family: "Lato", sans-serif;
  }
  .card {
    position: absolute;
    left: 180px;
    width: 840px;
    height: 480px;
    background: var(--card);
    overflow: hidden;
  }
  .card--front { top: 83px; }
  .card--back { top: 638px; }

  .brand {
    position: absolute;
    left: 0;
    width: 100%;
    display: flex;
    flex-direction: column;
    align-items: center;
  }
  .brand__mark { background: var(--brand-grey); }
  .brand__name {
    color: var(--brand-blue);
    font-weight: 700;
    white-space: nowrap;
    line-height: 1.1;
  }
  .card--front .brand { top: 28px; }
  .card--front .brand__mark { width: 70px; height: 70px; margin-bottom: 16px; }
  .card--front .brand__name { font-size: 32px; }
  .card--back .brand { top: 128px; }
  .card--back .brand__mark { width: 104px; height: 104px; margin-bottom: 40px; }
  .card--back .brand__name { font-size: 44px; }

  .credentials {
    position: absolute;
    left: 0;
    top: 176px;
    width: 100%;
    display: flex;
    justify-content: center;
    align-items: center;
    gap: 10px;
    color: var(--brand-grey);
    font-size: 15px;
    letter-spacing: 0.5px;
  }
  .credentials__badge {
    width: 34px;
    height: 34px;
    border-radius: 50%;
    background: var(--brand-grey);
  }

  .rule {
    position: absolute;
    left: 0;
    top: 239px;
    width: 100%;
    height: 4px;
    background: var(--brand-grey);
  }
  .info-band {
    position: absolute;
    left: 0;
    top: 247px;
    width: 100%;
    height: 233px;
    background: var(--brand-blue);
    color: var(--ink-light);
  }
  .person {
    position: absolute;
    left: 152px;
    top: 80px;
    width: 248px;
    text-align: center;
  }
  .person__name {
    font-size: 29px;
    font-weight: 700;
    letter-spacing: -0.5px;
    padding-bottom: 3px;
    border-bottom: 2px solid var(--ink-light);
    white-space: nowrap;
  }
  .person__post {
    font-size: 18px;
    font-weight: 400;
    letter-spacing: 0;
    margin-left: 4px;
  }
  .person__title {
    margin-top: 6px;
    font-size: 19px;
    letter-spacing: 4px;
  }
  .divider {
    position: absolute;
    left: 420px;
    top: 70px;
    width: 2px;
    height: 96px;
    background: var(--ink-light);
  }
  .contacts {
    position: absolute;
    left: 444px;
    top: 68px;
    margin: 0;
    padding: 0;
    list-style: none;
  }
  .contacts__item {
    display: flex;
    align-items: center;
    height: 34px;
    font-size: 20px;
  }
  .contacts__icon {
    width: 26px;
    height: 22px;
    margin-right: 8px;
    fill: none;
    stroke: var(--ink-light);
    stroke-width: 1.6;
  }
</style>
</head>
<body>

<section class="card card--front">
  <div class="brand">
    <div class="brand__mark"></div>
    <div class="brand__name">Your Loan Scout</div>
  </div>
  <div class="credentials">
    <div class="credentials__badge" role="img" aria-label="TLCA accredited member badge"></div>
    <span>Credit Rep Number 381749</span>
  </div>
  <div class="rule"></div>
  <div class="info-band">
    <div class="person">
      <div class="person__name">Daniel Hartley<span class="person__post">JP</span></div>
      <div class="person__title">Broker/Director</div>
    </div>
    <div class="divider"></div>
    <ul class="contacts">
      <li class="contacts__item">
        <svg class="contacts__icon" viewBox="0 0 26 22">
          <path d="M2 8 Q13 0 24 8 L20 10 L17 7 H9 L6 10 Z" fill="#fff"/>
          <path d="M5 11 H21 V19 H5 Z" fill="#fff"/>
          <circle cx="13" cy="15" r="2.5" fill="#0b78be" stroke="none"/>
        </svg>
        <span>0400 555 218</span>
      </li>
      <li class="contacts__item">
        <svg class="contacts__icon" viewBox="0 0 26 22">
          <rect x="1.5" y="4" width="23" height="14"/>
          <path d="M1.5 4 L13 12 L24.5 4 M1.5 18 L10 10.5 M24.5 18 L16 10.5"/>
        </svg>
        <span>dan@yourloanscout.com.au</span>
      </li>
      <li class="contacts__item">
        <svg class="contacts__icon" viewBox="0 0 26 22">
          <circle cx="13" cy="11" r="9.5"/>
          <ellipse cx="13" cy="11" rx="4" ry="9.5"/>
          <path d="M3.5 11 H22.5 M5 6 H21 M5 16 H21"/>
        </svg>
        <span>www.yourloanscout.com.au</span>
      </li>
    </ul>
  </div>
</section>

<section class="card card--back">
  <div class="brand">
    <div class="brand__mark"></div>
    <div class="brand__name">Your Loan Scout</div>
  </div>
</section>

</body>
</html>
```